Bref créative
Businesscard + stationary
outstand and cretive master piece!
Bright & Fun-filled
Mariana Tolvaldi
www.pixelharbor-exemplo.com.br
contato@pixelharbor-exemplo.com.br
You need to add to business card:
Skype: pixelharbor.online
Twitter: @PixelHarboron
Secondary text to go below logo: Desenvolvimento Web
On the back of business card goes only the logo and some nice art if applyable
This is the new website layout, so please follow this style to create the businesscard and stationary.
This is teh original logo file in EPS
this is another version of teh logo

```html
<!DOCTYPE html>
<html lang="pt-BR">
<head>
<meta charset="utf-8">
<title>pixelharbor – Cartão de visita</title>
<link rel="stylesheet" href="https://fonts.googleapis.com/css2?family=Source+Sans+3:wght@300;400;600&display=swap">
<style>
  :root {
    --stage: #e6e6e3;
    --card-dark: #231f20;
    --card-blue: #5aace0;
    --accent-blue: #5aace0;
    --text-light: #ffffff;
    --text-muted: #d6d6d6;
    --shadow: rgba(0, 0, 0, 0.22);
  }
  * { box-sizing: border-box; margin: 0; padding: 0; }
  html, body {
    width: 1200px; height: 901px; overflow: hidden;
    background: var(--stage);
    font-family: "Source Sans 3", "Myriad Pro", sans-serif;
  }
  .stage {
    position: relative; width: 1200px; height: 901px;
    display: flex; align-items: center; justify-content: center; gap: 60px;
  }
  .card {
    position: relative; width: 500px; height: 286px;
    box-shadow: 0 8px 22px var(--shadow);
    overflow: hidden;
  }

  /* front */
  .card--front { background: var(--card-dark); color: var(--text-light); }
  .card--front .base-band {
    position: absolute; left: 0; right: 0; bottom: 0; height: 26px;
    background: var(--accent-blue);
  }
  .brand { position: absolute; display: flex; flex-direction: column; }
  .brand__name {
    font-weight: 300; letter-spacing: -0.5px; line-height: 1;
    white-space: nowrap;
  }
  .brand__tagline { font-weight: 300; white-space: nowrap; }

  .card--front .brand { left: 32px; top: 122px; }
  .card--front .brand__name { font-size: 34px; }
  .card--front .brand__tagline { font-size: 13px; color: var(--text-muted); margin-top: 2px; margin-left: 2px; }

  .divider {
    position: absolute; left: 232px; top: 52px; width: 2px; height: 170px;
    background: var(--accent-blue);
  }
  .contact { position: absolute; left: 258px; top: 58px; }
  .contact__name { font-size: 21px; font-weight: 400; margin-bottom: 12px; }
  .contact__list { list-style: none; font-size: 12.5px; font-weight: 300; color: var(--text-muted); }
  .contact__list li { display: flex; align-items: center; gap: 8px; line-height: 19px; white-space: nowrap; }
  .contact__list svg { width: 11px; height: 11px; flex: none; fill: var(--accent-blue); }

  /* back */
  .card--back { background: var(--card-blue); color: var(--text-light); }
  .card--back .brand { left: 0; right: 0; top: 78px; align-items: center; }
  .card--back .brand__name { font-size: 62px; }
  .card--back .brand__tagline { font-size: 21px; margin-top: 4px; }
  .social {
    position: absolute; left: 0; right: 0; bottom: 26px;
    display: flex; justify-content: center; align-items: center; gap: 12px;
    font-size: 12.5px; font-weight: 300;
  }
  .social__item { display: flex; align-items: center; gap: 6px; }
  .social__mark { width: 9px; height: 9px; background: var(--text-light); }
  .social__sep { width: 1px; height: 16px; background: var(--text-light); }
</style>
</head>
<body>
<main class="stage">

  <section class="card card--front" aria-label="Frente do cartão">
    <div class="brand">
      <span class="brand__name">pixelharbor</span>
      <span class="brand__tagline">Desenvolvimento Web</span>
    </div>
    <div class="divider"></div>
    <div class="contact">
      <p class="contact__name">Mariana Tolvaldi</p>
      <ul class="contact__list">
        <li><svg viewBox="0 0 12 12"><path d="M3 1h2l1 3-1.5 1a6 6 0 0 0 2.5 2.5L8 6l3 1v2a2 2 0 0 1-2 2A8 8 0 0 1 1 3a2 2 0 0 1 2-2z"/></svg>11 3000 0142</li>
        <li><svg viewBox="0 0 12 12"><rect x="3" y="0.5" width="6" height="11" rx="1.2"/></svg>11 9000 0287</li>
        <li><svg viewBox="0 0 12 12"><path d="M0.5 2.5h11v7h-11z M1 3l5 3.5L11 3" stroke="#231f20" stroke-width="0.8"/></svg>contato@pixelharbor-exemplo.com.br</li>
        <li><svg viewBox="0 0 12 12"><circle cx="6" cy="6" r="5.5"/></svg>www.pixelharbor-exemplo.com.br</li>
      </ul>
    </div>
    <div class="base-band"></div>
  </section>

  <section class="card card--back" aria-label="Verso do cartão">
    <div class="brand">
      <span class="brand__name">pixelharbor</span>
      <span class="brand__tagline">Desenvolvimento Web</span>
    </div>
    <div class="social">
      <span class="social__item"><span class="social__mark"></span>pixelharbor.online</span>
      <span class="social__sep"></span>
      <span class="social__item"><span class="social__mark"></span>@PixelHarboron</span>
    </div>
  </section>

</main>
</body>
</html>
```